Business Card Design

We need a business card designed for a new company based in Melbourne called KPo solutions. KPo solutions provides management consulting specialising in the health and social services sector.

KPo solutions offer a unique set of specialist skills │dealing with all levels of government │ unique communication skills│intimate knowledge of the health sector │solutions tailored to unique circumstances.

KPo solutions takes on a select number of clients at any one time, this ensures that your organisation receives the attention required. On larger projects, KPo solutions join up with other consultants to bring specialist skills to a project.
Updates

This is the first time I have used Pattern Hive and thank you all for responding. The variation is amazing and makes it hard to decide. I have to ask some of my friends to give me their views. The response is fantastic. The one I pick will basically be the most visually appealing

Industry/Entity Type

Management Consulting

Contact Information for Business Card

Martin Hollis, Principal, KPo solutions, 14 Calloway Ave, Westbridge VIC 3094, 0438 712 304, martinh@kposolutions.com.au, www.kposolutions.com.au

```html
<!DOCTYPE html>
<html lang="en">
<head>
<meta charset="utf-8">
<title>KPo solutions — Business Card</title>
<link rel="stylesheet" href="https://fonts.googleapis.com/css2?family=Lato:wght@400;700;900&family=Roboto+Slab:wght@400&display=swap">
<style>
  :root {
    --backdrop: #2b2b2d;
    --card-red: #c8162c;
    --card-red-deep: #8e0f1f;
    --ink-dark: #1a0508;
    --ink-white: #ffffff;
    --ink-soft: #f1d7da;
    --ink-grey: #d9c6c8;
    --pattern-tint: rgba(255, 255, 255, 0.14);
    --pattern-dark: rgba(60, 0, 10, 0.25);
  }
  * { box-sizing: border-box; margin: 0; padding: 0; }
  html, body {
    width: 1200px; height: 900px; overflow: hidden;
    background: var(--backdrop);
    font-family: "Lato", Arial, sans-serif;
  }
  .business-card {
    position: absolute; left: 100px; top: 164px;
    width: 1000px; height: 572px;
    background: linear-gradient(120deg, var(--card-red) 0%, #b3132a 55%, var(--card-red-deep) 100%);
    box-shadow: 0 20px 50px rgba(0,0,0,0.55);
    overflow: hidden;
  }
  .pattern { position: absolute; border-radius: 2px; }
  .pattern--grid { left: 18px; top: 178px; width: 62px; height: 130px; background: var(--pattern-tint); }
  .pattern--column { left: 520px; top: 28px; width: 40px; height: 170px; background: var(--pattern-dark); }

  .owner-name {
    position: absolute; left: 130px; top: 150px;
    font-family: "Roboto Slab", Georgia, serif;
    font-size: 22px; color: var(--ink-dark); letter-spacing: 0.5px;
  }
  .brand-name {
    position: absolute; left: 128px; top: 178px;
    font-size: 56px; font-weight: 700; color: var(--ink-white);
    letter-spacing: 1px; line-height: 1;
  }
  .brand-tagline {
    position: absolute; left: 210px; top: 248px;
    font-size: 12px; font-weight: 700; color: var(--ink-white);
    letter-spacing: 1.6px; text-transform: uppercase;
  }
  .strengths {
    position: absolute; left: 124px; top: 330px; width: 400px;
    list-style: none;
    font-size: 26px; font-weight: 700; color: var(--ink-soft); line-height: 1.15;
  }
  .strengths li { padding-left: 22px; text-indent: -22px; }
  .strengths li::before { content: "- "; }

  .holder {
    position: absolute; right: 70px; top: 52px; text-align: right;
  }
  .holder__name { font-size: 32px; font-weight: 900; color: var(--ink-white); letter-spacing: 0.5px; }
  .holder__role { font-size: 18px; font-weight: 700; color: var(--ink-dark); letter-spacing: 1px; }

  .web-feature {
    position: absolute; right: 70px; top: 205px;
    font-size: 28px; font-weight: 900; color: var(--ink-white);
  }
  .web-feature span { color: var(--ink-dark); }

  .contacts {
    position: absolute; left: 540px; top: 300px; width: 390px; list-style: none;
    font-size: 20px; font-weight: 700; color: var(--ink-dark);
  }
  .contacts li { display: flex; align-items: center; gap: 14px; height: 40px; white-space: nowrap; }
  .contacts .contacts__web { font-size: 23px; font-weight: 900; }
  .contacts .contacts__address { color: var(--ink-grey); padding-left: 40px; }
  .contacts svg { width: 26px; height: 22px; flex: none; }
</style>
</head>
<body>
  <main class="business-card">
    <div class="pattern pattern--grid" role="img" aria-label="Faint grid of small plus signs"></div>
    <div class="pattern pattern--column" role="img" aria-label="Vertical row of dark plus signs"></div>

    <p class="owner-name">Martin Hollis</p>
    <p class="brand-name">KPo solutions</p>
    <p class="brand-tagline">Health &amp; Social Services Consulting</p>

    <ul class="strengths">
      <li>Dealing with all levels of government</li>
      <li>Unique communication skills</li>
      <li>Intimate knowledge of the health sector</li>
      <li>Solutions tailored to unique circumstances.</li>
    </ul>

    <div class="holder">
      <p class="holder__name">MARTIN HOLLIS</p>
      <p class="holder__role">PRINCIPAL</p>
    </div>

    <p class="web-feature">www.kposolutions<span>.com.au</span></p>

    <ul class="contacts">
      <li class="contacts__web">www.kposolutions.com.au</li>
      <li>
        <svg viewBox="0 0 26 22" aria-hidden="true"><path d="M2 8c0-4 22-4 22 0v2h-6V7H8v3H2z" fill="#f1d7da"/><rect x="6" y="11" width="14" height="9" rx="2" fill="#f1d7da"/><circle cx="13" cy="15.5" r="2.4" fill="#a8122a"/></svg>
        0438 712 304
      </li>
      <li>
        <svg viewBox="0 0 26 22" aria-hidden="true"><rect x="1" y="3" width="24" height="16" fill="#f1d7da"/><path d="M1 3l12 9 12-9" fill="none" stroke="#a8122a" stroke-width="1.6"/></svg>
        martinh@kposolutions.com.au
      </li>
      <li class="contacts__address">14 Calloway Ave, Westbridge VIC 3094</li>
    </ul>
  </main>
</body>
</html>
```